Bref créative
Church stationary, door hangers, envelopes (large & small), and banner
Harvest Light Fellowship
We are a church concerned with our community, interested in reaching out to them with the love of God.
Religion and Spirituality
A.) Business card and stationery:
The envelope sizes are the standard #10 letter envelope and the standard large envelope size that a 8 1/2" x 11" piece of paper can fit into.
Please present designs with the current logo image that we have uploaded. Notice there are two styles, one with the church name in the logo and one image without it. Our current business card uses the logo image with the name of the church in it. We want to see designs using both logo images.
Name on business card: Dwight L. Barlow
Designation: Pastor
Business address: 2738 Kessler Mill Rd.
Phone numbers:
803-628-xxxx cell (we can add this number later)
803-472-1958 office
E-mail and website:
pastor@harvestlightfw.org
www.harvestlightfw.org
B.) Door hanger:
The door hanger size is approximately 4 1/2" wide x 12" tall.
Sample is attached. The back side should contain a map showing the directions to the church, service times, and a simple message inviting them to church
C.) Banner:
This should be a horizontal banner to be printed on a vinyl sign approximately 3' x 5'.
Include Tagline: Sunday 3:00 pm, Wednesday 7:30 pm
The image will be the church logo and name of the church. Also, included on the sign will be the times of the services, listed above. We are looking at using a white background for this sign.
Please see scanned image of our current business card layout. We want to see the business card presented with the name "Harvest Light" as part of the image and apart and to the right of the image. Thanks for your designs.
This is our current stationary.
We have uploaded a zip file with the logo vector files i.e. eps files. Hope this helps.
Thanks,
TM
Door hanger sample

```html
<!DOCTYPE html>
<html lang="en">
<head>
<meta charset="utf-8">
<title>Harvest Light – Service Banner</title>
<link rel="stylesheet" href="https://fonts.googleapis.com/css2?family=Libre+Franklin:wght@400;600;800&family=Noto+Serif:wght@700&display=swap">
<style>
  :root {
    --page: #ecebe8;
    --paper: #ffffff;
    --gold: #b58e10;
    --gold-band: #b3901c;
    --ink: #1a1a1a;
    --sky-top: #a9c3e0;
    --sky-mid: #dde8f4;
    --page-light: #f6f3ec;
    --page-shade: #cbbfa9;
    --white-text: #ffffff;
  }
  html, body {
    margin: 0;
    width: 1200px;
    height: 782px;
    overflow: hidden;
    background: var(--page);
  }
  .banner {
    position: absolute;
    left: 96px;
    top: 82px;
    width: 1008px;
    height: 619px;
    background: var(--paper);
    box-shadow: 0 2px 8px rgba(0,0,0,0.15);
    overflow: hidden;
    font-family: "Libre Franklin", Arial, sans-serif;
  }
  .sky {
    position: absolute;
    left: 0; top: 0;
    width: 1008px;
    height: 250px;
    background: linear-gradient(to bottom, var(--sky-top) 0%, var(--sky-mid) 50%, var(--paper) 100%);
  }
  .hero-art {
    position: absolute;
    left: 60px;
    top: 40px;
    width: 852px;
    height: 190px;
    border-radius: 40% 40% 12px 12px / 30% 30% 12px 12px;
    background: linear-gradient(to bottom, var(--page-light) 0%, #ebe4d6 55%, var(--page-shade) 100%);
  }
  .church-mark {
    position: absolute;
    left: 30px;
    top: 258px;
    width: 190px;
    display: flex;
    flex-direction: column;
    align-items: center;
    gap: 10px;
  }
  .church-mark .mark-name {
    font-weight: 800;
    font-size: 24px;
    color: var(--gold);
    white-space: nowrap;
  }
  .church-mark .mark-square {
    width: 180px;
    height: 190px;
    background: var(--gold);
  }
  .headline {
    position: absolute;
    left: 293px;
    top: 256px;
    margin: 0;
    font-weight: 800;
    font-size: 58px;
    line-height: 67px;
    color: var(--gold);
  }
  .intro {
    position: absolute;
    left: 295px;
    top: 404px;
    margin: 0;
    font-family: "Noto Serif", Georgia, serif;
    font-weight: 700;
    font-size: 19px;
    line-height: 26px;
    color: var(--ink);
  }
  .service-times {
    position: absolute;
    left: 293px;
    top: 464px;
    margin: 0;
    font-weight: 800;
    font-size: 31px;
    color: var(--gold);
  }
  .rule {
    position: absolute;
    left: 0;
    top: 514px;
    width: 1008px;
    height: 2px;
    background: var(--gold-band);
  }
  .contact-band {
    position: absolute;
    left: 0;
    top: 523px;
    width: 1008px;
    height: 96px;
    background: var(--gold-band);
    color: var(--white-text);
    font-size: 17px;
    text-align: center;
    display: flex;
    flex-direction: column;
    justify-content: center;
    line-height: 1.45;
  }
</style>
</head>
<body>
  <section class="banner">
    <div class="sky"></div>
    <div class="hero-art" role="img" aria-label="Illustration of an open Bible glowing against a soft blue sky with sparkles"></div>

    <div class="church-mark">
      <div class="mark-name">Harvest Light</div>
      <div class="mark-square"></div>
    </div>

    <h1 class="headline">What does the<br>Bible say about...?</h1>
    <p class="intro">Discover the many answers that the<br>Bible has about life in today's ever-changing world!</p>
    <p class="service-times">Sunday 3:00 pm, Wednesday 7:30 pm</p>

    <div class="rule"></div>
    <footer class="contact-band">
      <div>2738 Kessler Mill Road, West Columbia, SC 29170</div>
      <div>Phone : 803-628-xxxx &nbsp;• Cell : 803 472 1958 &nbsp;• E-mail : pastor@harvestlightfw.org &nbsp;• www.harvestlightfw.org</div>
    </footer>
  </section>
</body>
</html>
```